Letterhead design for Dental Practice - Ashby Lane Dental Care

Letterhead for Private Dental Practice. To be used for all official correspondance and for printing treatment details on to be given to patients.

Target Market(s)

Private dental patients

Industry/Entity Type

Dental Clinic

Font styles to use
Other font styles liked:
• nexa-light

Colors
33a6d7
1c66ac
85abd2

Requirements
Must have
• info in the footer and header needs to be 3.5cm from upper/lower boader of paper, see photo in uploaded files
• info details:
• tel. 0115 947 3051
• email info@ashbylanedc.co.uk
• ashbylanedentalcare.co.uk
• 17b Ashby Lane West Bridgford Nottingham NG2 7QT
• nexa-light font as in uploaded logo files
Should not have
• No funny tooth pictures

```html
<!DOCTYPE html>
<html lang="en">
<head>
<meta charset="utf-8">
<title>Ashby Lane Dental Care – Letterhead</title>
<link rel="stylesheet" href="https://fonts.googleapis.com/css2?family=Open+Sans:wght@400;600&family=Quicksand:wght@400;500&display=swap">
<style>
  :root {
    --brand-blue: #1a9fdc;
    --brand-blue-soft: #85abd2;
    --charcoal: #4f4f51;
    --ink: #4a4a4a;
    --rule: #9a9a9a;
    --paper: #ffffff;
    --backdrop: #e4e4e4;
  }
  * { box-sizing: border-box; margin: 0; padding: 0; }
  html, body {
    width: 1040px; height: 1200px; overflow: hidden;
    background: var(--backdrop);
  }
  .letterhead {
    position: absolute; left: 53px; top: 0;
    width: 934px; height: 1200px;
    background: var(--paper);
    font-family: "Open Sans", Arial, sans-serif;
    color: var(--ink);
  }
  .side-band { position: absolute; left: 0; top: 0; width: 60px; height: 1200px; }

  .brand {
    position: absolute; right: 96px; top: 128px;
    display: flex; align-items: center; gap: 12px;
    font-family: "Quicksand", Arial, sans-serif;
    font-weight: 400; font-size: 30px; color: var(--brand-blue);
    letter-spacing: 0.5px;
  }
  .brand-dot { width: 16px; height: 16px; border-radius: 50%; background: var(--brand-blue); }

  .letter-body { position: absolute; left: 87px; width: 754px; font-size: 15px; line-height: 18px; }
  .issue-date { top: 212px; }
  .recipient { top: 248px; }
  .salutation { top: 352px; }
  .content { top: 408px; line-height: 27px; text-align: justify; hyphens: auto; }
  .content p + p { margin-top: 27px; }

  .closing { position: absolute; left: 87px; top: 811px; font-size: 15px; }
  .signature {
    display: block; width: 214px; height: 30px; margin-top: 18px;
    background: linear-gradient(90deg, rgba(74,74,74,0.15), rgba(74,74,74,0.05));
    border-radius: 4px;
  }
  .signatory-name { margin-top: 10px; font-size: 20px; font-weight: 600; color: #3a3a3a; }
  .signatory-role { margin-top: 4px; font-size: 15px; }

  .contact-row {
    position: absolute; top: 1097px; left: 83px; width: 756px;
    display: flex; justify-content: space-between; align-items: center;
    font-family: "Quicksand", Arial, sans-serif; font-size: 15px; color: #3c3c3c;
  }
  .contact-item { display: flex; align-items: center; gap: 9px; }
  .contact-item svg { width: 26px; height: 26px; flex: none; }
  .contact-item:first-child { margin-left: 12px; }
  .footer-rule { position: absolute; top: 1137px; left: 83px; width: 756px; height: 1px; background: var(--rule); }
  .address {
    position: absolute; top: 1157px; left: 0; width: 934px; text-align: center;
    font-family: "Quicksand", Arial, sans-serif; font-size: 15px; color: #3c3c3c;
  }
</style>
</head>
<body>
<main class="letterhead">
  <svg class="side-band" viewBox="0 0 60 1200" aria-hidden="true">
    <rect x="0" y="0" width="32" height="1200" fill="var(--brand-blue)"/>
    <polygon points="0,316 60,285 60,694 0,736" fill="var(--paper)"/>
    <polygon points="0,327 58,296 58,682 0,723" fill="var(--charcoal)"/>
    <polygon points="30,262 56,279 30,296" fill="var(--charcoal)"/>
  </svg>

  <div class="brand"><span class="brand-dot"></span>Ashby Lane Dental Care</div>

  <p class="letter-body issue-date">Issuing Date: May 5, 2018</p>
  <p class="letter-body recipient">Name Of Employee Mr. XYZABC<br>Address of Employee<br>Address Line 2 etc..</p>
  <p class="letter-body salutation">Dear Mr.XYZABC</p>

  <div class="letter-body content">
    <p>Lorem Ipsum has been the industry's standard dummy text ever since the 1500s, when an unknown printer took a galley of type and scrambled it to make a type specimen book. It has survived not only five centuries, but also the leap into electronic typesetting, remaining essentially unchanged. It was popularised in the 1960s with the release of Typeline sheets containing Lorem Ipsum passages, and more recently with desktop publishing software like Folio Layout including versions of Lorem Ipsum.</p>
    <p>Lorem Ipsum is simply dummy text of the printing and typesetting industry. Lorem Ipsum has been the industry's standard dummy text ever since the 1500s, when an unknown printer took a galley of type and scrambled it to make a type specimen book.</p>
    <p>It has survived not only five centuries, but also the leap into electronic typesetting, remaining essentially unchanged. It was popularised in the 1960s with the release of Typeline sheets containing Lorem IpsumIpsum passages.</p>
  </div>

  <div class="closing">
    <p>Yours Sincerely</p>
    <span class="signature" role="img" aria-label="Handwritten signature of Daniel Hart"></span>
    <p class="signatory-name">Daniel Hart</p>
    <p class="signatory-role">Managing Director</p>
  </div>

  <div class="contact-row">
    <span class="contact-item">
      <svg viewBox="0 0 26 26" aria-hidden="true"><circle cx="13" cy="13" r="12" fill="var(--brand-blue)"/><path d="M9.5 7.5l2 .3 1 3-1.4 1.1a7 7 0 0 0 3 3l1.1-1.4 3 1 .3 2c-.4.9-1.3 1.5-2.3 1.4C11.6 17.5 8.5 14.4 8.1 9.8c-.1-1 .5-1.9 1.4-2.3z" fill="#fff"/></svg>
      0115 947 3051
    </span>
    <span class="contact-item">
      <svg viewBox="0 0 26 26" aria-hidden="true"><circle cx="13" cy="13" r="12" fill="var(--brand-blue)"/><rect x="7.5" y="9" width="11" height="8" rx="1" fill="none" stroke="#fff" stroke-width="1.5"/><path d="M7.8 9.5L13 13.5l5.2-4" fill="none" stroke="#fff" stroke-width="1.5"/></svg>
      info@ashbylanedc.co.uk
    </span>
    <span class="contact-item">
      <svg viewBox="0 0 26 26" aria-hidden="true"><circle cx="13" cy="13" r="12" fill="var(--brand-blue)"/><circle cx="13" cy="13" r="6" fill="none" stroke="#fff" stroke-width="1.5"/><path d="M7 13h12M13 7c-2.5 3-2.5 9 0 12M13 7c2.5 3 2.5 9 0 12" fill="none" stroke="#fff" stroke-width="1.2"/></svg>
      www.ashbylanedentalcare.co.uk
    </span>
  </div>
  <div class="footer-rule"></div>
  <p class="address">17b Ashby Lane West&nbsp; Bridgford Nottingham NG2 7QT</p>
</main>
</body>
</html>
```